Business card for Mortgage broker business

I have already had the logo designed and am needing a great looking business card. My business focus is on servicing clients who may not be able to obtain finance through traditional lenders due to bad credit, short term employment or they just don't fit the banks profile. It needs to be professional, trust worthy but also have a caring fell about it.
I have provided files showing the green and black logo, the white logo(on white background so the file looks blank) and also a file with the white logo with a background of leaves that was made up which will probably be used for a website header.

Industry/Entity Type

Finance

Contact Information for Business Card

Marcus Dalby
Managing Director, Accredited Finance Broker(AFB)
Po Box 817, Pakenham VIC 3810
marcus@kestrelfunding.com.au
www.kestrelfunding.com.au
0438 216 507

Requirements
Nice to have
• I have added a picture of myself as I would like to see some designs with the pic in it, but I'm not sure if I want it on there with the logo's or just the logo's

```html
<!DOCTYPE html>
<html lang="en">
<head>
<meta charset="utf-8">
<title>Kestrel Funding – Business Card</title>
<link href="https://fonts.googleapis.com/css2?family=Montserrat:wght@400;500;600&display=swap" rel="stylesheet">
<style>
  :root {
    --page-bg: #ece9e4;
    --card-white: #ffffff;
    --brand-green: #2f8a5a;
    --name-green: #1f6b3a;
    --ink: #2b2b2b;
    --muted: #6d6d6d;
    --leaf-deep: #3a1410;
    --leaf-red: #9c2f1e;
    --leaf-orange: #d8772c;
    --leaf-olive: #8e9a3a;
  }
  * { box-sizing: border-box; margin: 0; padding: 0; }
  html, body { width: 1200px; height: 900px; overflow: hidden; }
  body {
    background: var(--page-bg);
    font-family: "Montserrat", Arial, sans-serif;
    position: relative;
  }
  .card {
    position: absolute;
    width: 540px;
    height: 309px;
    border-radius: 4px;
    box-shadow: 0 6px 18px rgba(0,0,0,.15);
    overflow: hidden;
  }
  .card--front { left: 40px; top: 296px; }
  .card--back  { left: 620px; top: 296px; background: var(--card-white); }

  .front-photo {
    position: absolute; inset: 0;
    background:
      radial-gradient(ellipse at 30% 20%, var(--leaf-orange) 0%, transparent 45%),
      radial-gradient(ellipse at 70% 15%, var(--leaf-red) 0%, transparent 50%),
      radial-gradient(ellipse at 35% 60%, var(--leaf-olive) 0%, transparent 45%),
      linear-gradient(120deg, #6b2a17 0%, #a2522a 40%, var(--leaf-deep) 100%);
  }
  .front-brand {
    position: absolute;
    left: 0; right: 0; top: 150px;
    text-align: center;
    color: var(--card-white);
    font-weight: 500;
    font-size: 30px;
    letter-spacing: 1px;
  }

  .back-brand {
    position: absolute;
    right: 34px; top: 40px;
    color: var(--brand-green);
    font-weight: 500;
    font-size: 24px;
  }
  .holder { position: absolute; left: 34px; top: 150px; }
  .holder-name { color: var(--name-green); font-size: 14px; font-weight: 500; letter-spacing: .5px; }
  .holder-role { color: var(--ink); font-size: 11px; margin-top: 2px; }

  .address {
    position: absolute; left: 56px; top: 202px;
    color: var(--muted); font-size: 10.5px; line-height: 1.3;
  }
  .contact-list {
    position: absolute; left: 34px; top: 236px;
    list-style: none; font-size: 10.5px; color: var(--muted);
  }
  .contact-list li { display: flex; align-items: center; height: 15px; }
  .contact-list svg { width: 10px; height: 10px; margin-right: 12px; fill: var(--ink); }
  .contact-list .web { color: var(--name-green); font-weight: 600; }

  .social {
    position: absolute; right: 34px; top: 150px;
    color: var(--muted); font-size: 11px;
  }
</style>
</head>
<body>

<section class="card card--front">
  <div class="front-photo" role="img" aria-label="Soft-focus photograph of red and orange autumn maple leaves"></div>
  <div class="front-brand">Kestrel Funding</div>
</section>

<section class="card card--back">
  <div class="back-brand">Kestrel Funding</div>

  <div class="holder">
    <p class="holder-name">YOUR NAME</p>
    <p class="holder-role">Position</p>
  </div>

  <p class="address">1275 North Ridge Rd<br>Suite 210-318 Kingsford, AZ</p>

  <ul class="contact-list">
    <li><svg viewBox="0 0 10 10"><path d="M2 0.5 L3.6 2.6 L2.7 3.6 Q3.8 5.9 6.4 7.3 L7.4 6.4 L9.5 8 L8.4 9.5 Q3.5 9 0.5 1.6 Z"/></svg>0417 352 908</li>
    <li><svg viewBox="0 0 10 10"><path d="M2.5 0 H7.5 V10 H2.5 Z M3.5 1 V8 H6.5 V1 Z"/></svg>0417 352 908</li>
    <li><svg viewBox="0 0 10 10"><path d="M0 4.5 L10 0 L6 10 L4.6 5.4 Z"/></svg>info@kestrelfunding.com</li>
    <li class="web"><svg viewBox="0 0 10 10"><circle cx="5" cy="5" r="5"/><path d="M0 5 H10 M5 0 V10" stroke="#fff" stroke-width=".8"/></svg>www.kestrelfunding.com</li>
  </ul>

  <p class="social">/KestrelFunding</p>
</section>

</body>
</html>
```